House flipping business web site needed

pinecrestholdingsgroup.com.
I am a residential developer in Northern NJ and I am looking for a fresh new updated website. I have an intro video about my company being made now. I don't update it very often but I want an easy format that I can add update photos to on projects I have worked on or homes I renovate for sale.

Target Market(s)

investors into my projects so a portfolio , people looking to sell their homes to me.

Industry/Entity Type

Real Estate Development

Number of Pages Required

4 page

Font styles to use
Serif

Colors
33b8a4
39a9d7
cadf82

Requirements
Must have
• space for an intro video about my company
• a portfolio with pictures and information about each project
• Markets we serve- Alder County
• My logo- already created
• SEO
• Yes I would like this to function over all platforms. Phone, computer, all platforms.
• history and background page
• I am looking for a completed page that I can upload to the site that hosts my website
Nice to have
• I want something creative, easy to navigate. modern.

```html
<!DOCTYPE html>
<html lang="en">
<head>
<meta charset="utf-8">
<title>Pinecrest Holdings Group</title>
<link href="https://fonts.googleapis.com/css2?family=Open+Sans:wght@400;600;700&family=Roboto+Condensed:wght@400;700&display=swap" rel="stylesheet">
<style>
:root{
  --blue:#29a3dc;
  --footer-blue:#0b8ecf;
  --green:#8cc63f;
  --ink:#222;
  --muted:#555;
  --soft-bg:#e9eefa;
  --card-bg:#f6f6f6;
  --card-line:#e2e2e2;
  --dark:#1b1b1b;
  --white:#fff;
}
*{box-sizing:border-box;margin:0;padding:0}
html,body{width:1200px;height:3005px;overflow:hidden}
body{position:relative;font-family:"Open Sans",sans-serif;color:var(--ink);background:var(--white)}
.cond{font-family:"Roboto Condensed",sans-serif}

/* header */
.site-header{position:absolute;left:0;top:0;width:1200px;height:160px;background:#f5f6f8}
.brand{position:absolute;left:96px;top:44px;display:flex;align-items:center;gap:12px}
.brand-dot{width:44px;height:44px;border-radius:50%;background:var(--blue)}
.brand-name{font-family:"Roboto Condensed",sans-serif;font-size:22px;font-weight:700;color:#1e5f8f;line-height:1.1;width:150px}
.contact-item{position:absolute;top:30px;font-size:12px;color:#444}
.contact-item .label{display:flex;align-items:center;gap:8px;font-size:11px;letter-spacing:.5px;text-transform:uppercase}
.contact-item .value{margin-top:8px;font-size:13px;color:#1e5f8f}
.quote-btn{position:absolute;left:956px;top:32px;width:142px;height:38px;background:var(--green);color:#fff;font-size:12px;font-weight:600;display:flex;align-items:center;justify-content:center;text-transform:uppercase}
.main-nav{position:absolute;left:330px;top:106px;width:870px;height:54px;background:var(--blue)}
.nav-home{position:absolute;left:0;top:0;width:124px;height:54px;background:var(--green);clip-path:polygon(28px 0,100% 0,100% 100%,0 100%)}
.main-nav a{position:absolute;top:0;height:54px;line-height:54px;color:#fff;font-size:13px;text-decoration:none;text-transform:uppercase;transform:translateX(-50%)}

/* hero */
.hero{position:absolute;left:0;top:160px;width:1200px;height:526px;background:linear-gradient(180deg,#2e3b22 0%,#4d5a3a 45%,#6b6a5a 60%,#3f5a2a 85%,#587a32 100%)}
.hero-title{position:absolute;left:0;width:1200px;top:228px;text-align:center;color:#fff;font-size:50px;font-weight:700}
.hero-sub{position:absolute;left:0;width:1200px;top:290px;text-align:center;color:#fff;font-size:19px}
.dots{position:absolute;left:570px;top:335px;display:flex;gap:6px}
.dots span{width:12px;height:12px;border-radius:50%;border:2px solid #fff}
.dots span:first-child{background:#fff}

/* about */
.about{position:absolute;left:0;top:686px;width:1200px;height:430px;background:var(--soft-bg)}
.video{position:absolute;left:96px;top:66px;width:502px;height:294px;background:linear-gradient(160deg,#f4f4f4,#dcdcdc);border:3px solid #d0d0d0}
.video-play{position:absolute;left:218px;top:114px;width:66px;height:44px;background:#222;border-radius:8px}
.video-play::after{content:"";position:absolute;left:26px;top:13px;border-left:16px solid #fff;border-top:9px solid transparent;border-bottom:9px solid transparent}
.video-bar{position:absolute;left:16px;right:16px;bottom:14px;height:24px;background:#333;border-radius:3px}
.video-bar i{position:absolute;left:8px;top:10px;width:250px;height:4px;background:var(--blue)}
.about h2{position:absolute;left:628px;top:62px;font-size:36px;font-weight:700;color:var(--ink)}
.about h3{position:absolute;left:628px;top:110px;font-size:25px;font-weight:400}
.about-text{position:absolute;left:628px;top:156px;width:472px;font-size:11.5px;line-height:21px;color:#444}
.about-text p+p{margin-top:6px}
.read-more{position:absolute;left:628px;top:324px;width:112px;height:36px;background:var(--green);color:#fff;font-size:12px;display:flex;align-items:center;justify-content:center;text-transform:uppercase}

/* projects */
.projects-title{position:absolute;left:0;width:1200px;top:1154px;text-align:center;font-size:33px;font-weight:400}
.card{position:absolute;width:322px;height:308px;background:var(--card-bg);border:1px solid var(--card-line)}
.card-photo{height:196px}
.card-body{padding:14px 14px 0;font-size:12px;color:var(--muted)}
.card-title{font-size:13px;color:#333;text-transform:uppercase}
.card-loc{margin-top:8px;display:flex;align-items:center;gap:6px;font-size:13px;color:#333}
.card-desc{margin-top:10px;line-height:19px}

/* map */
.map{position:absolute;left:0;top:1920px;width:1200px;height:406px;background:linear-gradient(135deg,#a9c2d6 0%,#e6e2d6 35%,#e9e4d8 60%,#c8d9a8 80%,#e6e2d6 100%)}

/* news */
.news-title{position:absolute;left:96px;top:2378px;font-size:25px;font-weight:400;color:#333}
.news-title span{color:#1e7fc0}
.news-arrows{position:absolute;left:1050px;top:2384px;display:flex;gap:12px;font-size:16px;color:#333}
.news-photo{position:absolute;width:188px;height:164px;top:2432px}
.news-body{position:absolute;top:2428px;width:272px;font-size:11px;line-height:20px;color:#555}
.news-body h4{font-size:16px;font-weight:400;color:#333;margin-bottom:12px;white-space:nowrap}
.news-date{color:#1e7fc0;font-weight:600;margin-bottom:6px}
.news-more{margin-top:16px;color:#333;font-size:12px}

/* footer */
.site-footer{position:absolute;left:0;top:2660px;width:1200px;height:284px;background:var(--footer-blue);color:#fff}
.site-footer h5{position:absolute;top:48px;font-family:"Roboto Condensed",sans-serif;font-size:19px;font-weight:400;text-transform:uppercase}
.f-row{position:absolute;display:flex;gap:12px;font-size:13px;line-height:20px}
.socials{position:absolute;left:96px;top:218px;display:flex;gap:8px}
.socials span{width:24px;height:24px;border-radius:50%;background:#fff}
.tweet{position:absolute;left:410px;width:240px;font-size:11px;line-height:17px;display:flex;gap:10px}
.tweet i{flex:none;width:20px;height:20px;background:#fff;margin-top:2px}
.tweet small{display:block;margin-top:8px;font-size:11px}
.newsletter-text{position:absolute;left:698px;top:92px;width:230px;font-size:11px;line-height:17px}
.newsletter-input{position:absolute;left:698px;top:134px;width:242px;height:40px;background:#fff;color:#666;font-size:11px;padding:12px 10px}
.newsletter-btn{position:absolute;left:698px;top:188px;width:102px;height:40px;background:#000;color:#fff;font-size:11px;display:flex;align-items:center;justify-content:center;text-transform:uppercase}
.quick-links{position:absolute;left:992px;top:92px;list-style:none;font-size:12px;line-height:24px;text-transform:uppercase}
.bottom-bar{position:absolute;left:0;top:2944px;width:1200px;height:61px;background:var(--dark);color:#ddd;font-size:12px;text-align:center;line-height:61px}
</style>
</head>
<body>

<header class="site-header">
  <div class="brand"><span class="brand-dot"></span><span class="brand-name">Pinecrest Holdings Group</span></div>
  <div class="contact-item" style="left:550px">
    <div class="label"><svg width="12" height="12" viewBox="0 0 24 24"><path fill="#555" d="M6.6 10.8a15 15 0 0 0 6.6 6.6l2.2-2.2c.3-.3.7-.4 1-.2 1.1.4 2.3.6 3.6.6.6 0 1 .4 1 1V20c0 .6-.4 1-1 1A17 17 0 0 1 3 4c0-.6.4-1 1-1h3.5c.6 0 1 .4 1 1 0 1.3.2 2.5.6 3.6.1.3 0 .7-.2 1z"/></svg>Call us anytime</div>
    <div class="value">973-555-0148</div>
  </div>
  <div class="contact-item" style="left:730px">
    <div class="label"><svg width="13" height="10" viewBox="0 0 26 20"><rect x="1" y="1" width="24" height="18" fill="none" stroke="#555" stroke-width="2"/><path d="M1 1l12 10L25 1" fill="none" stroke="#555" stroke-width="2"/></svg>Email us</div>
    <div class="value">info@pinecrestholdingsgroup.com</div>
  </div>
  <div class="quote-btn">Request a quote</div>
  <nav class="main-nav">
    <div class="nav-home"></div>
    <a style="left:74px">Home</a>
    <a style="left:186px">About us</a>
    <a style="left:300px">Portfolio</a>
    <a style="left:452px">Our services</a>
    <a style="left:562px">Blog</a>
    <a style="left:696px">Contact us</a>
  </nav>
</header>

<section class="hero" role="img" aria-label="Photo of a weathered white house among trees and lawn">
  <div class="hero-title cond">PINECREST HOLDINGS GROUP</div>
  <div class="hero-sub cond">INVESTING IN OUR NEIGHBORHOODS</div>
  <div class="dots"><span></span><span></span><span></span></div>
</section>

<section class="about">
  <div class="video" role="img" aria-label="Company intro video with logo poster">
    <div class="video-play"></div>
    <div class="video-bar"><i></i></div>
  </div>
  <h2 class="cond">ABOUT OUR COMPANY</h2>
  <h3 class="cond">Pinecrest Holdings Group</h3>
  <div class="about-text">
    <p>We are a team of experienced home buyers and renovators in the Alder County area. Our specialty is purchasing distressed homes and property. We then collaborate with the best talents in the Northern Valley to renovate those properties and transform them into the best house in the neighborhood.</p>
    <p>As a result we create equity, a return on investment and most importantly we give home buyers a worry free property that provides a better way of life and hope for their future. We only work in the Alder County area so we are local</p>
  </div>
  <div class="read-more">Read more</div>
</section>

<h2 class="projects-title cond">OUR PROJECT</h2>

<article class="card" style="left:96px;top:1218px"><div class="card-photo" role="img" aria-label="Photo of a two-storey house on a stone wall" style="background:linear-gradient(180deg,#c9ccd0,#9a8f80 70%,#6e6a5a)"></div><div class="card-body"><div class="card-title">Nemo enim ipsam voluptatem</div><div class="card-loc"><svg width="10" height="13" viewBox="0 0 10 14"><path d="M5 0a5 5 0 0 0-5 5c0 4 5 9 5 9s5-5 5-9a5 5 0 0 0-5-5zm0 7a2 2 0 1 1 0-4 2 2 0 0 1 0 4z" fill="#333"/></svg>Millbrook</div><div class="card-desc">Many upgrades to this home, Added a new full bath, family room, office, kitchenette</div></div></article>
<article class="card" style="left:436px;top:1218px"><div class="card-photo" role="img" aria-label="Photo of a small blue cottage among trees" style="background:linear-gradient(180deg,#3f5a2e,#6f8fa0 60%,#4f6b36)"></div><div class="card-body"><div class="card-title">Nemo enim ipsam voluptatem</div><div class="card-loc"><svg width="10" height="13" viewBox="0 0 10 14"><path d="M5 0a5 5 0 0 0-5 5c0 4 5 9 5 9s5-5 5-9a5 5 0 0 0-5-5zm0 7a2 2 0 1 1 0-4 2 2 0 0 1 0 4z" fill="#333"/></svg>Ashford Hills</div><div class="card-desc">Many upgrades to this home, Added a new full bath, family room, office, kitchenette</div></div></article>
<article class="card" style="left:778px;top:1218px"><div class="card-photo" role="img" aria-label="Photo of a white house above a stone retaining wall" style="background:linear-gradient(180deg,#d8dde2,#a9a89c 60%,#6f8a46)"></div><div class="card-body"><div class="card-title">Nemo enim ipsam voluptatem</div><div class="card-loc"><svg width="10" height="13" viewBox="0 0 10 14"><path d="M5 0a5 5 0 0 0-5 5c0 4 5 9 5 9s5-5 5-9a5 5 0 0 0-5-5zm0 7a2 2 0 1 1 0-4 2 2 0 0 1 0 4z" fill="#333"/></svg>Millbrook</div><div class="card-desc">Many upgrades to this home, Added a new full bath, family room, office, kitchenette</div></div></article>
<article class="card" style="left:96px;top:1552px"><div class="card-photo" role="img" aria-label="Photo of a renovated kitchen with wood cabinets" style="background:linear-gradient(180deg,#7a3a1e,#a8622e 50%,#6a3418)"></div><div class="card-body"><div class="card-title">Nemo enim ipsam voluptatem</div><div class="card-loc"><svg width="10" height="13" viewBox="0 0 10 14"><path d="M5 0a5 5 0 0 0-5 5c0 4 5 9 5 9s5-5 5-9a5 5 0 0 0-5-5zm0 7a2 2 0 1 1 0-4 2 2 0 0 1 0 4z" fill="#333"/></svg>Kestrel Falls</div><div class="card-desc">Many upgrades to this home, Added a new full bath, family room, office, kitchenette</div></div></article>
<article class="card" style="left:436px;top:1552px"><div class="card-photo" role="img" aria-label="Photo of a grey colonial house with lawn" style="background:linear-gradient(180deg,#b9c4cc,#8a9096 55%,#5e7a3a)"></div><div class="card-body"><div class="card-title">Nemo enim ipsam voluptatem</div><div class="card-loc"><svg width="10" height="13" viewBox="0 0 10 14"><path d="M5 0a5 5 0 0 0-5 5c0 4 5 9 5 9s5-5 5-9a5 5 0 0 0-5-5zm0 7a2 2 0 1 1 0-4 2 2 0 0 1 0 4z" fill="#333"/></svg>Kestrel Falls</div><div class="card-desc">Many upgrades to this home, Added a new full bath, family room, office, kitchenette</div></div></article>
<article class="card" style="left:778px;top:1552px"><div class="card-photo" role="img" aria-label="Photo of a house under construction with an excavator" style="background:linear-gradient(180deg,#9bb0c4,#c9c2b4 45%,#5a4a3a)"></div><div class="card-body"><div class="card-title">Nemo enim ipsam voluptatem</div><div class="card-loc"><svg width="10" height="13" viewBox="0 0 10 14"><path d="M5 0a5 5 0 0 0-5 5c0 4 5 9 5 9s5-5 5-9a5 5 0 0 0-5-5zm0 7a2 2 0 1 1 0-4 2 2 0 0 1 0 4z" fill="#333"/></svg>Ashford Hills</div><div class="card-desc">Many upgrades to this home, Added a new full bath, family room, office, kitchenette</div></div></article>

<section class="map" role="img" aria-label="Map showing project locations with markers"></section>

<section>
  <h2 class="news-title cond">LATEST <span>NEWS</span></h2>
  <div class="news-arrows"><span>&larr;</span><span>&rarr;</span></div>
  <div class="news-photo" role="img" aria-label="Photo of a red house beside a dumpster" style="left:96px;background:linear-gradient(180deg,#a9b8c4,#7a3a2e 55%,#5e7a3a)"></div>
  <div class="news-body" style="left:308px"><h4>Nulla at diam ornare, aliquam urna</h4><div class="news-date">MAY 25, 2016</div><p>Nulla at diam ornare, aliquam urna vel, commodo urna. Nam id risus a est luctus consectetur quis eget libero. Suspendisse potenti. Pellentesque habitant morbi tristique senectus</p><div class="news-more">Read More +</div></div>
  <div class="news-photo" role="img" aria-label="Photo of a renovated living room and kitchen" style="left:628px;width:186px;background:linear-gradient(180deg,#d8d8d4,#8a8680 55%,#3a3430)"></div>
  <div class="news-body" style="left:840px"><h4>Nulla at diam ornare, aliquam urna</h4><div class="news-date">MAY 25, 2016</div><p>Nulla at diam ornare, aliquam urna vel, commodo urna. Nam id risus a est luctus consectetur quis eget libero. Suspendisse potenti. Pellentesque habitant morbi tristique senectus</p><div class="news-more">Read More +</div></div>
</section>

<footer class="site-footer">
  <h5 style="left:96px">Contact us</h5>
  <div class="f-row" style="left:96px;top:92px"><svg width="14" height="20" viewBox="0 0 10 14"><path d="M5 0a5 5 0 0 0-5 5c0 4 5 9 5 9s5-5 5-9a5 5 0 0 0-5-5zm0 7a2 2 0 1 1 0-4 2 2 0 0 1 0 4z" fill="#fff"/></svg><div style="margin-left:8px">Pinecrest Holdings Group<br>Alder County | 973-555-0148</div></div>
  <div class="f-row" style="left:96px;top:144px"><svg width="16" height="16" viewBox="0 0 24 24"><path fill="#fff" d="M6.6 10.8a15 15 0 0 0 6.6 6.6l2.2-2.2c.3-.3.7-.4 1-.2 1.1.4 2.3.6 3.6.6.6 0 1 .4 1 1V20c0 .6-.4 1-1 1A17 17 0 0 1 3 4c0-.6.4-1 1-1h3.5c.6 0 1 .4 1 1 0 1.3.2 2.5.6 3.6.1.3 0 .7-.2 1z"/></svg><div style="margin-left:8px">Phone: 973-555-0148</div></div>
  <div class="f-row" style="left:96px;top:180px"><svg width="16" height="14" viewBox="0 0 26 20"><rect x="1" y="1" width="24" height="18" fill="none" stroke="#fff" stroke-width="2"/><path d="M1 1l12 10L25 1" fill="none" stroke="#fff" stroke-width="2"/></svg><div style="margin-left:8px">info@pinecrestholdingsgroup.com</div></div>
  <div class="socials"><span></span><span></span><span></span><span></span></div>

  <h5 style="left:410px">Latest tweet`s</h5>
  <div class="tweet" style="top:94px"><i></i><div><b>@Pinecrest Holdings</b> Fusce suscit varius mi. Cum sociis natoque<small>1 day ago</small></div></div>
  <div class="tweet" style="top:160px"><i></i><div><b>@Pinecrest Holdings</b> Fusce suscit varius mi. Cum sociis natoque<small>1 day ago</small></div></div>

  <h5 style="left:698px">Join our newsletter</h5>
  <p class="newsletter-text">Excepteur sint occaecat cupidatat non proident, sunt in culpa qui</p>
  <div class="newsletter-input">Enter Name</div>
  <div class="newsletter-btn">Subscribe</div>

  <h5 style="left:992px">Quick links</h5>
  <ul class="quick-links"><li>Home</li><li>About</li><li>Contact</li><li>Portfolio</li></ul>
</footer>

<div class="bottom-bar">Copyright 2016 | All Rights Reserved -- Pinecrest Holdings Group</div>

</body>
</html>
```